The Velmora Company Sweet Packaging Design

The Velmora Trading Company is looking for a logo and label design for an upcoming line of honey based health and beauty products that are sourced from the Polynesian Islands (Hawaii, New Zealand, Fiji etc.).The brand will be premium price positioned and the design and packaging should exude class and quality.The design should be flexible enough to add products from future locations.We would like to see the design across three different product forms:1. Glass Honey Jar (main product)2. Hand cream / lotion (pump bottle, or lotion tube)3. Small box (e.g. throat lozenges / gum packet etc.)The Polynesia Islands are unique and exotic locations; the design/packaging should reflect this but should not be overly complicated. Each individual island has their own distinct culture and history but they have many commonalities which fall under "Polynesian Culture". The Velmora Trading Company is an umbrella brand that should be able to support a growing number of products.Possible designs may (but are not required to) incorporate local flowers (Hawaii / Hibiscus flower, New Zealand / Manuka Flower etc.) into the design, Islands, and boutique feel (elegant classy looking)Please feel free to ask more questions for further guidance but we really want to see where the creative process can take us outside of what we have already considered internally.
Updates

We needed to modify our idea slightly because of competition.

We needed extend to get a few more ideas. We did not want to copy our competition and needed to add a part to our design that we did not include before.

Target Market(s)

Health conscious people. Honey lovers.

Font styles to use
Serif
Sans Serif
Decorative

Colors

Designer to choose colors to be used in the design.

Requirements
Must have
• a little tribal look. because its 100% polynesian Honey.. it would be nice to have the fee of that in the design..

```html
<!DOCTYPE html>
<html lang="en">
<head>
<meta charset="utf-8">
<title>The Velmora Trading Company – Label Set</title>
<link href="https://fonts.googleapis.com/css2?family=Josefin+Sans:wght@700&display=swap" rel="stylesheet">
<style>
  :root {
    --paper: #ffffff;
    --ink: #1b1a16;
    --ink-soft: #24221c;
    --gold: #f0d38a;
    --gold-deep: #e2b85a;
    --type-light: #ffffff;
  }
  html, body {
    margin: 0;
    padding: 0;
    width: 1200px;
    height: 1000px;
    overflow: hidden;
    background: var(--paper);
  }
  .label-sheet {
    display: block;
    width: 1200px;
    height: 1000px;
  }
  .band-fill { fill: var(--ink); }
  .badge-outline { fill: none; stroke: var(--gold); stroke-width: 3; }
  .badge-face { fill: var(--ink); stroke: var(--gold); stroke-width: 5; }
  .seal-ring { fill: var(--paper); stroke: var(--gold); stroke-width: 3; }
  .seal-face { fill: var(--ink); }
  .seal-inner { fill: none; stroke: var(--gold); stroke-width: 5; }
  .brand-dot { fill: var(--gold-deep); }
  .rule { stroke: var(--gold); stroke-width: 2; }
  .brand-name {
    font-family: "Josefin Sans", sans-serif;
    font-weight: 700;
    fill: var(--type-light);
    text-anchor: middle;
    letter-spacing: 0;
  }
  .brand-name--lg { font-size: 19px; }
  .brand-name--md { font-size: 18px; }
  .brand-name--sm { font-size: 15px; }
</style>
</head>
<body>
<svg class="label-sheet" viewBox="0 0 1200 1000" xmlns="http://www.w3.org/2000/svg">

  <!-- Jar wrap label -->
  <g class="jar-wrap">
    <rect class="band-fill" x="26" y="67" width="1138" height="398" role="img" aria-label="Dark band with a faint gold honeycomb pattern"/>
    <polygon class="badge-outline" points="595,97 741.4,181.5 741.4,350.5 595,435 448.6,350.5 448.6,181.5"/>
    <polygon class="badge-face" points="595,111 729.2,188.5 729.2,343.5 595,421 460.8,343.5 460.8,188.5"/>
    <circle class="brand-dot" cx="595" cy="215" r="26"/>
    <text class="brand-name brand-name--lg" x="595" y="307">THE VELMORA</text>
    <text class="brand-name brand-name--lg" x="595" y="335">TRADING COMPANY</text>
    <line class="rule" x1="556" y1="364" x2="632" y2="364"/>
    <line class="rule" x1="556" y1="370" x2="632" y2="370"/>
  </g>

  <!-- Lotion tube band -->
  <g class="tube-band">
    <rect class="band-fill" x="24" y="656" width="791" height="162" role="img" aria-label="Dark band with a faint gold honeycomb pattern"/>
    <polygon class="badge-outline" points="420,600 538.6,668.5 538.6,805.5 420,874 301.4,805.5 301.4,668.5"/>
    <polygon class="badge-face" points="420,612 528.3,674.5 528.3,799.5 420,862 311.7,799.5 311.7,674.5"/>
    <circle class="brand-dot" cx="420" cy="695" r="22"/>
    <text class="brand-name brand-name--sm" x="420" y="774">THE VELMORA</text>
    <text class="brand-name brand-name--sm" x="420" y="797">TRADING COMPANY</text>
    <line class="rule" x1="389" y1="820" x2="451" y2="820"/>
    <line class="rule" x1="389" y1="825" x2="451" y2="825"/>
  </g>

  <!-- Box seal -->
  <g class="box-seal">
    <circle class="seal-ring" cx="996" cy="728" r="157"/>
    <circle class="seal-face" cx="996" cy="728" r="149"/>
    <circle class="seal-inner" cx="996" cy="728" r="135"/>
    <circle class="brand-dot" cx="996" cy="670" r="24"/>
    <text class="brand-name brand-name--md" x="996" y="766">THE VELMORA</text>
    <text class="brand-name brand-name--md" x="996" y="792">TRADING COMPANY</text>
    <line class="rule" x1="960" y1="818" x2="1032" y2="818"/>
    <line class="rule" x1="960" y1="824" x2="1032" y2="824"/>
  </g>

</svg>
</body>
</html>
```